i would like a business card to leave with customers and potential customers for electrical work and for the supply and install of reverse cycle airconditioning in the domestic and commercial market.
I own my own business and im a sole trader. I have an a'class electrical lisence and also a refrigeration lisence so i am
able to offer complete installations in airconditioning by a fully qualified and lisenced tradesman.
im looking for something that comes across as unique and professional.
i had the coluor black and some gold in mind but open to any coluors.
something like Beacon Electrical & Refrigeration
or Beacon Air.
i will use this design on a business card to advertise through summer to help generate installs through the busy season.

Target Market(s)

Mainly domestic house holds through summer who are in need of airconditioning and reliable information to acomadate thier cooling and heating requirements

Industry/Entity Type

Electrical

Requirements
Must have
• Business name- Beacon
My name- Peter Wollaston
My mobile no- 0457 819 302
My email- prwollaston@tarvel.com.au
Installation & Decomissioning of aiconditioning split systems
LIC NO: KTR 407516
Nice to have
• Beacon Electrical & Refrigeration

```html
<!DOCTYPE html>
<html lang="en">
<head>
<meta charset="utf-8">
<title>Beacon Electrical &amp; Refrigeration — Business Card</title>
<link rel="stylesheet" href="https://fonts.googleapis.com/css2?family=Almendra&family=Open+Sans:wght@600&family=Arimo&display=swap">
<style>
  :root {
    --page-bg: #ffffff;
    --card-top: #1d1d1d;
    --card-bottom: #050505;
    --gold: #c98f2e;
    --gold-deep: #9a6a1c;
    --mark-faint: rgba(255, 255, 255, 0.04);
  }
  html, body {
    margin: 0;
    width: 1200px;
    height: 900px;
    overflow: hidden;
    background: var(--page-bg);
  }
  .card {
    position: absolute;
    left: 100px;
    top: 150px;
    width: 1000px;
    height: 600px;
    background: linear-gradient(160deg, var(--card-top), var(--card-bottom));
    color: var(--gold);
    box-shadow: 0 10px 30px rgba(0, 0, 0, 0.35);
    overflow: hidden;
  }
  .brand-square {
    position: absolute;
    left: 60px;
    top: 205px;
    width: 150px;
    height: 150px;
    background: linear-gradient(135deg, var(--gold), var(--gold-deep));
  }
  .faint-square {
    position: absolute;
    left: 380px;
    top: 220px;
    width: 170px;
    height: 170px;
    background: var(--mark-faint);
  }
  .business-name {
    position: absolute;
    left: 235px;
    top: 150px;
    margin: 0;
    font-family: "Almendra", serif;
    font-weight: 400;
    font-size: 44px;
    letter-spacing: 1px;
  }
  .contact {
    position: absolute;
    right: 70px;
    top: 240px;
    text-align: right;
    font-family: "Arimo", sans-serif;
    font-size: 30px;
    line-height: 1.25;
  }
  .owner-name {
    margin: 0 0 4px;
    font-family: "Open Sans", sans-serif;
    font-weight: 600;
    font-size: 42px;
  }
  .contact p { margin: 0; }
  .email {
    margin-top: 26px !important;
    font-size: 34px;
  }
  .service {
    position: absolute;
    left: 60px;
    right: 70px;
    bottom: 70px;
    margin: 0;
    font-family: "Arimo", sans-serif;
    font-size: 29px;
    text-align: right;
  }
</style>
</head>
<body>
  <div class="card">
    <div class="faint-square" aria-hidden="true"></div>
    <div class="brand-square" aria-hidden="true"></div>
    <h1 class="business-name">Beacon Electrical &amp; Refrigeration</h1>
    <div class="contact">
      <h2 class="owner-name">Peter Wollaston</h2>
      <p class="licence">LIC NO: KTR 407516</p>
      <p class="phone">0457 819 302</p>
      <p class="email">prwollaston@tarvel.com.au</p>
    </div>
    <p class="service">Installation &amp; Decomissioning of aiconditioning split systems</p>
  </div>
</body>
</html>
```